Business Cards

Need a neat design for a new business card

Industry/Entity Type

Residential Construction

Contact Information for Business Card

Company Name- KOVE Construction Inc.
Owner- Marcus Tolliver
Phone number- (555)203-7481
Email- kovecohomes@brindlemail.example
Facebook- www.socialpage.example/kovecohomes

Colors
fefdec

```html
<!DOCTYPE html>
<html lang="en">
<head>
<meta charset="utf-8">
<title>KOVE Construction – Business Card</title>
<link rel="stylesheet" href="https://fonts.googleapis.com/css2?family=Arimo:wght@400;700&display=swap">
<style>
  :root {
    --backdrop: #26282d;
    --card: #121212;
    --ink: #fefdec;
    --emboss: #3b3b3b;
    --hairline: #2b2b2b;
  }
  * { margin: 0; padding: 0; box-sizing: border-box; }
  html, body {
    width: 1200px; height: 1200px; overflow: hidden;
    background: var(--backdrop);
    font-family: "Arimo", Arial, sans-serif;
  }
  .sheet {
    width: 1200px; height: 1200px;
    display: flex; flex-direction: column; align-items: center; justify-content: center;
    gap: 40px;
  }
  .card {
    position: relative;
    width: 960px; height: 548px;
    background: var(--card);
    border: 1px solid var(--hairline);
  }
  /* Front side */
  .card-front {
    display: flex; align-items: center; justify-content: center;
  }
  .front-brand {
    display: flex; align-items: center; gap: 22px;
    color: var(--emboss);
    font-size: 58px; font-weight: 400; letter-spacing: 0.06em;
  }
  .front-brand .brand-square {
    width: 34px; height: 34px; background: var(--emboss);
  }
  /* Back side */
  .back-brand {
    position: absolute; top: 74px; right: 70px;
    display: flex; align-items: center; gap: 16px;
    color: var(--ink);
    font-size: 30px; font-weight: 400; letter-spacing: 0.05em;
  }
  .back-brand .brand-square {
    width: 22px; height: 22px; background: var(--ink);
  }
  .person {
    position: absolute; left: 70px; top: 250px;
    color: var(--ink);
  }
  .person-name { font-size: 38px; font-weight: 700; line-height: 1.1; }
  .person-role { font-size: 24px; font-weight: 400; margin-top: 6px; }
  .contacts {
    position: absolute; left: 300px; bottom: 60px;
    list-style: none; color: var(--ink);
    font-size: 25px; line-height: 1.35;
  }
  .contacts li { display: flex; align-items: center; gap: 12px; }
  .contacts svg { width: 20px; height: 20px; flex: none; }
</style>
</head>
<body>
<main class="sheet">
  <section class="card card-front" aria-label="Card front">
    <div class="front-brand"><span class="brand-square"></span><span>KOVE Construction</span></div>
  </section>

  <section class="card card-back" aria-label="Card back">
    <div class="back-brand"><span class="brand-square"></span><span>KOVE Construction</span></div>

    <div class="person">
      <p class="person-name">Marcus Tolliver</p>
      <p class="person-role">Owner</p>
    </div>

    <ul class="contacts">
      <li>
        <svg viewBox="0 0 20 20" aria-hidden="true"><path fill="#fefdec" d="M5 2l3 3-2 2c1 2.5 2.5 4 5 5l2-2 3 3-2 3C8 15.5 4.5 12 2 5z"/></svg>
        <span>(555)203-7481</span>
      </li>
      <li>
        <svg viewBox="0 0 20 20" aria-hidden="true"><rect x="2" y="4" width="16" height="12" fill="#fefdec"/><path d="M2 4l8 7 8-7" fill="none" stroke="#121212" stroke-width="1.6"/></svg>
        <span>kovecohomes@brindlemail.example</span>
      </li>
      <li>
        <svg viewBox="0 0 20 20" aria-hidden="true"><circle cx="10" cy="10" r="8" fill="#fefdec"/></svg>
        <span>www.socialpage.example/kovecohomes</span>
      </li>
    </ul>
  </section>
</main>
</body>
</html>
```